Saucy Velvet Impz Business Card

We need business cards designed for our consultants to use and hand out to customers.
We are an Adult party plan company (like Crelvaware but sex toys and lingerie)
We would like bright colours pinks, purples.
The cards need our logo
Space for the reps phone number email address and name.
We need our website on it www.saucyvelvetimps.com.au

```html
<!DOCTYPE html>
<html lang="en">
<head>
<meta charset="UTF-8">
<title>Saucy Velvet Impz Parties – Business Card</title>
<link href="https://fonts.googleapis.com/css2?family=Great+Vibes&family=Open+Sans:wght@400;600&display=swap" rel="stylesheet">
<style>
  :root {
    --backdrop: #ece6ea;
    --magenta: #d6249f;
    --magenta-deep: #b5138a;
    --orchid: #e063c0;
    --pink-soft: #f2a6d8;
    --band-black: #141214;
    --band-grey: #3a3739;
    --ink: #1a0f17;
    --brand-pink: #f06fc3;
  }
  * { box-sizing: border-box; margin: 0; padding: 0; }
  html, body { width: 1200px; height: 1014px; overflow: hidden; }
  body {
    background: var(--backdrop);
    display: flex;
    align-items: center;
    justify-content: center;
    gap: 90px;
    font-family: "Open Sans", sans-serif;
  }
  .card {
    position: relative;
    width: 400px;
    height: 700px;
    border-radius: 6px;
    overflow: hidden;
    box-shadow: 0 10px 30px rgba(60, 20, 50, 0.25);
  }

  /* Front */
  .card-front {
    background:
      radial-gradient(circle at 75% 30%, rgba(255,255,255,0.18), transparent 40%),
      radial-gradient(circle at 20% 70%, rgba(255,255,255,0.12), transparent 35%),
      linear-gradient(160deg, var(--magenta) 0%, var(--orchid) 50%, var(--magenta) 100%);
  }
  .rep-name {
    position: absolute;
    top: 46px;
    right: 40px;
    font-family: "Great Vibes", cursive;
    font-size: 40px;
    color: var(--ink);
    text-align: right;
  }
  .rep-title {
    position: absolute;
    top: 96px;
    right: 96px;
    font-size: 19px;
    font-weight: 600;
    color: var(--ink);
  }
  .mascot-area {
    position: absolute;
    left: 80px;
    top: 180px;
    width: 240px;
    height: 340px;
    border-radius: 110px 110px 20px 20px;
    background: linear-gradient(180deg, var(--pink-soft) 0%, rgba(242,166,216,0.6) 55%, rgba(232,80,170,0.7) 100%);
  }
  .contact {
    position: absolute;
    left: 34px;
    right: 34px;
    bottom: 36px;
    font-size: 18px;
    line-height: 1.5;
    color: var(--ink);
  }
  .contact .phone { padding-left: 62px; }

  /* Back */
  .card-back {
    background: linear-gradient(90deg, var(--magenta-deep) 0%, var(--orchid) 40%, var(--magenta) 100%);
  }
  .brand-band {
    position: absolute;
    top: 0;
    bottom: 0;
    left: 130px;
    width: 140px;
    background: linear-gradient(90deg, var(--band-black) 0%, var(--band-grey) 45%, var(--band-black) 100%);
    display: flex;
    align-items: center;
    justify-content: center;
  }
  .brand-lockup {
    display: flex;
    align-items: center;
    gap: 18px;
    transform: rotate(90deg);
    white-space: nowrap;
  }
  .brand-dot {
    width: 26px;
    height: 26px;
    border-radius: 50%;
    background: var(--brand-pink);
  }
  .brand-name {
    font-family: "Great Vibes", cursive;
    font-size: 54px;
    color: var(--brand-pink);
  }
</style>
</head>
<body>
  <section class="card card-front">
    <p class="rep-name">Delphine Marrow</p>
    <p class="rep-title">Manager</p>
    <div class="mascot-area" role="img" aria-label="Pink silhouette of the brand's little devil mascot"></div>
    <div class="contact">
      <p class="phone">phone: 555.014.2286</p>
      <p class="email">delphine@saucyvelvetimps.com.au</p>
      <p class="website">www.saucyvelvetimps.com.au</p>
    </div>
  </section>

  <section class="card card-back">
    <div class="brand-band">
      <div class="brand-lockup">
        <span class="brand-dot"></span>
        <span class="brand-name">Saucy Velvet Impz Parties</span>
      </div>
    </div>
  </section>
</body>
</html>
```